Home page design for Drone video business (the Business focusses on home videos for realtors)

Dear reader,

*I NEED DESIGNS OF ALL THE PAGES*
We need a first design of a homepage and of 4 other pages of the website of a business that sells drone video services. All the pages will need to be in the similar design style.
The video's are targeted at consumers that want to sell there home and would like to have a cool drone video of photos of their home.

How does the website look:
- has a navbar on top
- A cool looking banner of an areal drone.
- A Big header: with company name: SkyNestReels
- A smaller subheader: We film your home to increase your chances of sale
- Then a section with a Big header: How does it work
- In this section a place for a vimeo explainitory video
- Then a similar navbar styled bar with a phone number and a email address
- Then a section where the videos porfolio is displayed in a cool way
- Inside this sectiona header: Our work

- A section with header: Why us?
- 4 symbols here with a subheader and some lorum ipsum text underneath (see wireframe images)

- Under that a: Contact us
- where you can put in name, email, phone, message box and a send button

- At the bottom a footer with phone number and a fake address for now.

Be creative. Use creative but serious color.
Use a serious font. Make it a sharp design. Sharp lines. Not to dark design and not to light design.

The wireframes are the same kind of images.
PLEASE PUT IN DESIGNS OF ALL THE PAGES

Good luck

Target Market(s)

People that want to sell home and want to make a cool drone video or photos of their home.

Industry/Entity Type

Business

Contact Information for Business Card

Milo Brenning
milo@skynestreels.example
+31647283915

Logo Text

SkyNestReels

Number of Pages Required

1 page

Font styles to use
Sans Serif

Requirements
Must have
• All the sections as explained in the instructions.
• The nav bar should have an about us, services, portfolio and a contact us buttons.
• See instruction for details.
• Must include designs of the front page, contact us, our services, portfolio and contact us.
• If you do add some designs for the "about us", "services", "prices", "portfolio" and "contact us" pages, you make a way better chance of winning the competition.
Nice to have
• designs for the other pages as described at the Must haves. You make a better chance of winning if you include them. Look at the wireframes to see the mockups for those pages. think creative about what kind of sections and design should be included in those pages.
Should not have
• bad designs.

```html
<!DOCTYPE html>
<html lang="en">
<head>
<meta charset="utf-8">
<title>SkyNestReels – Gallery</title>
<link rel="stylesheet" href="https://fonts.googleapis.com/css2?family=Open+Sans:wght@400;600;700;800&display=swap">
<style>
  :root{
    --ink:#2b2550;
    --panel:#ffffff;
    --page:#e5e5e5;
    --accent:#f3c071;
    --caption:#5a5a5a;
    --frame:#dcdcdc;
    --active:#e7748c;
    --foot:#000000;
    --foot-text:#a9a9a9;
    --social:#333333;
  }
  *{box-sizing:border-box;margin:0;padding:0}
  html,body{width:1200px;height:1200px;overflow:hidden;background:#fff;font-family:"Open Sans",sans-serif}
  .canvas{position:relative;width:1200px;height:1200px}
  .site-header{position:absolute;left:0;top:0;width:1200px;height:66px;background:#fff}
  .brand{position:absolute;left:136px;top:14px;font-size:30px;font-weight:700;color:var(--ink);letter-spacing:1px}
  .brand-rule{position:absolute;left:214px;top:0;width:1px;height:66px;background:#eee}
  .main-nav{position:absolute;right:132px;top:24px;display:flex;gap:23px}
  .main-nav a{font-size:13px;font-weight:600;color:var(--ink);letter-spacing:1.5px;text-decoration:none}
  .content-band{position:absolute;left:79px;top:66px;width:1042px;height:833px;background:var(--page)}
  .sidebar{position:absolute;left:132px;top:97px;width:129px;height:748px;background:var(--ink);border-radius:2px 0 0 2px}
  .side-item{height:84px;border-bottom:1px solid #3a3462;display:flex;flex-direction:column;align-items:center;justify-content:center;gap:5px;color:#fff;font-size:10px;font-weight:600;position:relative}
  .side-item.active::after{content:"";position:absolute;right:0;top:36px;border:6px solid transparent;border-right-color:#fff}
  .gallery{position:absolute;left:261px;top:97px;width:557px;height:748px;background:var(--panel);border-radius:0 2px 2px 0}
  .filters{position:absolute;left:23px;top:24px;display:flex;gap:15px}
  .select{width:117px;height:33px;border:1px solid #e2e2e2;border-radius:2px;display:flex;align-items:center;justify-content:space-between;padding:0 10px 0 11px;font-size:10px;color:#999}
  .grid{position:absolute;left:23px;top:79px;display:grid;grid-template-columns:repeat(3,158px);column-gap:20px;row-gap:35px}
  .card{height:134px;position:relative}
  .thumb{width:158px;height:120px;border:1px solid var(--frame);border-radius:3px;padding:3px;background:#fff}
  .card.active .thumb{border-color:var(--active)}
  .shot{width:100%;height:100%;position:relative;display:flex;align-items:center;justify-content:center}
  .night{background:
    radial-gradient(ellipse 45% 40% at 68% 50%, rgba(214,178,60,.75), rgba(214,178,60,0) 70%),
    radial-gradient(ellipse 30% 25% at 30% 70%, rgba(170,210,120,.6), rgba(170,210,120,0) 70%),
    linear-gradient(180deg,#3b4a48 0%,#2c3633 45%,#1c2219 100%)}
  .dusk{background:
    radial-gradient(ellipse 40% 30% at 50% 58%, rgba(40,45,90,.9), rgba(40,45,90,0) 75%),
    linear-gradient(180deg,#8a7fae 0%,#c99aab 35%,#343a66 62%,#56607c 85%,#8a93a3 100%)}
  .day{background:
    radial-gradient(ellipse 50% 30% at 50% 52%, rgba(150,125,105,.8), rgba(150,125,105,0) 75%),
    linear-gradient(180deg,#9cbbd8 0%,#b9c9d6 22%,#a58d7a 45%,#d6d2ca 72%,#6f9448 84%,#5e8a3a 100%)}
  .brick{background:
    radial-gradient(ellipse 55% 35% at 50% 50%, rgba(160,130,100,.85), rgba(160,130,100,0) 75%),
    linear-gradient(180deg,#5c6a5a 0%,#a48f78 30%,#b39c84 60%,#6f8a4a 85%,#5f7c3c 100%)}
  .play{width:30px;height:30px;border-radius:50%;background:rgba(255,255,255,.22)}
  .play.big{width:38px;height:38px;background:#fff;display:flex;align-items:center;justify-content:center}
  .caption{position:absolute;left:0;top:126px;font-size:11px;font-weight:700;color:var(--caption)}
  .contact-card{position:absolute;left:840px;top:97px;width:229px;height:213px;background:var(--accent);border-radius:2px;text-align:center;color:#111;padding-top:40px}
  .contact-card .label{font-size:16px;font-weight:600;display:flex;align-items:center;justify-content:center;gap:7px}
  .contact-card .value{font-size:19px;font-weight:700;margin-top:2px}
  .contact-card .value.small{font-size:15px}
  .contact-card .block+.block{margin-top:42px}
  .site-footer{position:absolute;left:79px;top:899px;width:1042px;height:301px;background:var(--foot);text-align:center}
  .foot-nav{margin-top:57px;display:flex;justify-content:center;gap:32px}
  .foot-nav a{color:#fff;font-size:12px;font-weight:700;letter-spacing:1.3px;text-decoration:none}
  .foot-brand{margin-top:22px;font-size:26px;font-weight:800;color:#555;letter-spacing:.5px}
  .foot-text{width:490px;margin:6px auto 0;font-size:10px;line-height:15px;color:var(--foot-text);letter-spacing:.3px}
  .copyright{margin-top:5px;font-size:10px;color:var(--foot-text);letter-spacing:.5px}
  .social{margin-top:26px;display:flex;justify-content:center;gap:13px}
  .social span{width:34px;height:34px;border-radius:50%;background:var(--social)}
</style>
</head>
<body>
<div class="canvas">
  <header class="site-header">
    <div class="brand">SNR</div>
    <div class="brand-rule"></div>
    <nav class="main-nav"><a href="#">About us</a><a href="#">Our Service</a><a href="#">Portfolio</a><a href="#">Contact</a></nav>
  </header>

  <div class="content-band"></div>

  <aside class="sidebar">
    <div class="side-item">
      <svg width="22" height="19" viewBox="0 0 22 19"><rect x="1" y="1" width="20" height="17" fill="none" stroke="#fff" stroke-width="2"/><path d="M3 16l5-7 4 5 3-3 4 5z" fill="#fff"/><circle cx="15" cy="6" r="2" fill="#fff"/></svg>
      Image Gallery
    </div>
    <div class="side-item active">
      <svg width="24" height="18" viewBox="0 0 24 18"><circle cx="5" cy="4" r="3.5" fill="#fff"/><circle cx="12" cy="4" r="3.5" fill="#fff"/><rect x="1" y="9" width="15" height="8" fill="#fff"/><path d="M17 11l6-3v10l-6-3z" fill="#fff"/></svg>
      Video Gallery
    </div>
  </aside>

  <main class="gallery">
    <div class="filters">
      <div class="select">Latest to Old <svg width="8" height="14" viewBox="0 0 8 14"><path d="M4 1l3 4H1zM4 13l3-4H1z" fill="#333"/></svg></div>
      <div class="select">Select Category <svg width="8" height="14" viewBox="0 0 8 14"><path d="M4 1l3 4H1zM4 13l3-4H1z" fill="#333"/></svg></div>
    </div>
    <div class="grid">
      <div class="card active"><div class="thumb"><div class="shot night" role="img" aria-label="Two-storey house lit at night"><div class="play big"><svg width="12" height="14" viewBox="0 0 12 14"><path d="M1 1l10 6-10 6z" fill="#222"/></svg></div></div></div><div class="caption">Lorem lipsum dolor amiet</div></div>
      <div class="card"><div class="thumb"><div class="shot dusk" role="img" aria-label="Blue house with garage at dusk"><div class="play"></div></div></div><div class="caption">Lorem lipsum dolor amiet</div></div>
      <div class="card"><div class="thumb"><div class="shot day" role="img" aria-label="Suburban house with lawn by day"><div class="play"></div></div></div><div class="caption">Lorem lipsum dolor amiet</div></div>
      <div class="card"><div class="thumb"><div class="shot day" role="img" aria-label="Suburban house with lawn by day"><div class="play"></div></div></div><div class="caption">Lorem lipsum dolor amiet</div></div>
      <div class="card"><div class="thumb"><div class="shot brick" role="img" aria-label="Brick family house with garden"><div class="play"></div></div></div><div class="caption">Lorem lipsum dolor amiet</div></div>
      <div class="card"><div class="thumb"><div class="shot night" role="img" aria-label="Two-storey house lit at night"><div class="play"></div></div></div><div class="caption">Lorem lipsum dolor amiet</div></div>
      <div class="card"><div class="thumb"><div class="shot dusk" role="img" aria-label="Blue house with garage at dusk"><div class="play"></div></div></div><div class="caption">Lorem lipsum dolor amiet</div></div>
      <div class="card"><div class="thumb"><div class="shot night" role="img" aria-label="Two-storey house lit at night"><div class="play"></div></div></div><div class="caption">Lorem lipsum dolor amiet</div></div>
      <div class="card"><div class="thumb"><div class="shot brick" role="img" aria-label="Brick family house with garden"><div class="play"></div></div></div><div class="caption">Lorem lipsum dolor amiet</div></div>
      <div class="card"><div class="thumb"><div class="shot night" role="img" aria-label="Two-storey house lit at night"><div class="play"></div></div></div><div class="caption">Lorem lipsum dolor amiet</div></div>
      <div class="card"><div class="thumb"><div class="shot day" role="img" aria-label="Suburban house with lawn by day"><div class="play"></div></div></div><div class="caption">Lorem lipsum dolor amiet</div></div>
      <div class="card"><div class="thumb"><div class="shot dusk" role="img" aria-label="Blue house with garage at dusk"><div class="play"></div></div></div><div class="caption">Lorem lipsum dolor amiet</div></div>
    </div>
  </main>

  <section class="contact-card">
    <div class="block">
      <div class="label"><svg width="18" height="18" viewBox="0 0 24 24"><path d="M6.6 10.8a15.1 15.1 0 006.6 6.6l2.2-2.2a1 1 0 011-.25 11.4 11.4 0 003.6.57 1 1 0 011 1V20a1 1 0 01-1 1A17 17 0 013 4a1 1 0 011-1h3.5a1 1 0 011 1 11.4 11.4 0 00.57 3.6 1 1 0 01-.25 1z" fill="var(--ink)"/></svg>Call</div>
      <div class="value">+31 647283915</div>
    </div>
    <div class="block">
      <div class="label"><svg width="21" height="14" viewBox="0 0 21 14"><rect width="21" height="14" fill="var(--ink)"/><path d="M1 1l9.5 7L20 1" fill="none" stroke="var(--accent)" stroke-width="1.5"/></svg>Contact</div>
      <div class="value small">milo@skynestreels.example</div>
    </div>
  </section>

  <footer class="site-footer">
    <nav class="foot-nav"><a href="#">About us</a><a href="#">Our Service</a><a href="#">Portfolio</a><a href="#">Contact</a></nav>
    <div class="foot-brand">SKYNESTREELS</div>
    <p class="foot-text">Lorem ipsum dolor sit amet, consectetur adipiscing elit, sed do eiusmod tempor incididunt ut labore et dolore magna aliqua. Ut enim ad minim veniam, quis nostrud exercitation ullamco laboris nisi ut aliquip ex ea commodo consequat.</p>
    <p class="copyright">Copyright © 2016 skynestreels.example. All Rights Reserved.</p>
    <div class="social" aria-label="Social links"><span></span><span></span><span></span><span></span></div>
  </footer>
</div>
</body>
</html>
```